Need a flyer created for a charity motorcycle run.

I need a "First Annual Gus Tarn Black Friday Fun Run" flyer/poster created. It is to benefit the wild fire victims at Lake Berryessa where Gus spent all of his time on his boat. Gus died about 18 mos ago from brain cancer. I have a few pics of him on his Kestrow at Vandmere. I have the verbiage needed (due to Covid, there are several restrictions) but it needs some word smithing. This flyer will be emailed to those without social media accounts and also posted on FB as an invite so we can get a good count because space is limited.

Please make sure all designs have both pictures in them. Thanks

```html
<!DOCTYPE html>
<html lang="en">
<head>
<meta charset="utf-8">
<title>First Annual Gus Tarn Black Friday Fun Run</title>
<link rel="stylesheet" href="https://fonts.googleapis.com/css2?family=Alfa+Slab+One&family=Kaushan+Script&family=Crimson+Pro:wght@400;700&family=Special+Elite&family=Oswald:wght@600&display=swap">
<style>
  :root{
    --stage:#b3b3b3;
    --paper:#e6d8bd;
    --crimson:#8e1217;
    --crimson-deep:#6d0b0f;
    --cream:#efe4c8;
    --ink:#3b3128;
    --stitch:#4a3c30;
    --photo-sky:#6d7f95;
    --photo-bike:#2a3356;
  }
  *{box-sizing:border-box;margin:0;padding:0}
  html,body{width:1200px;height:952px;overflow:hidden;background:var(--stage)}
  .stage{position:relative;width:1200px;height:952px}

  /* FRONT */
  .flyer-front{position:absolute;left:50px;top:120px;width:510px;height:700px;background:var(--paper);overflow:hidden;box-shadow:0 6px 18px rgba(0,0,0,.35)}
  .front-band{position:absolute;left:0;top:0;width:100%;height:210px;background:linear-gradient(180deg,var(--crimson) 0%,var(--crimson-deep) 100%);border-bottom:3px solid var(--crimson-deep);z-index:2}
  .front-band::before{content:"";position:absolute;inset:10px 10px auto 10px;border-top:2px dashed rgba(239,228,200,.55)}
  .numeral{position:absolute;left:50px;top:40px;font:140px/1 "Alfa Slab One",serif;color:var(--cream)}
  .annual{position:absolute;left:160px;top:40px;font:46px/1 "Alfa Slab One",serif;color:var(--cream);letter-spacing:1px;white-space:nowrap;transform:rotate(-5deg);transform-origin:left bottom}
  .honoree{position:absolute;left:165px;top:98px;font:24px/1 "Kaushan Script",cursive;color:var(--cream);white-space:nowrap;transform:rotate(-5deg);transform-origin:left bottom}
  .fun-run{position:absolute;left:140px;top:150px;font:62px/1 "Alfa Slab One",serif;color:var(--cream);letter-spacing:2px;white-space:nowrap;z-index:3;text-shadow:2px 3px 0 rgba(0,0,0,.25);transform:rotate(-7deg);transform-origin:left bottom}
  .front-photo{position:absolute;left:0;top:190px;width:100%;height:310px;background:linear-gradient(160deg,var(--photo-sky) 0%,#8b7b6a 45%,var(--photo-bike) 100%)}
  .reg-badge{position:absolute;right:30px;top:222px;width:112px;height:112px;border-radius:50%;background:var(--crimson);border:4px dotted var(--crimson-deep);display:flex;flex-direction:column;align-items:center;justify-content:center;color:var(--cream);z-index:4;transform:rotate(-6deg)}
  .reg-badge .label{font:600 15px/1 "Oswald",sans-serif}
  .reg-badge .price{font:600 38px/1.1 "Oswald",sans-serif}
  .front-footer{position:absolute;left:0;top:470px;width:100%;height:230px;background:var(--paper)}
  .front-footer::before{content:"";position:absolute;inset:16px;border:2px dashed var(--stitch);border-top:none}
  .ride-line{position:absolute;left:30px;top:20px;font:42px/1 "Kaushan Script",cursive;color:#fff;white-space:nowrap;text-shadow:3px 3px 0 #1c1612;transform:rotate(-9deg);transform-origin:left bottom;z-index:3}
  .date-line{position:absolute;left:58px;top:112px;font:26px/1 "Alfa Slab One",serif;color:var(--crimson);white-space:nowrap;transform:rotate(-5deg);transform-origin:left bottom}
  .included{position:absolute;left:34px;top:172px;font:14px/1 "Alfa Slab One",serif;color:var(--crimson);white-space:nowrap;transform:rotate(-12deg);transform-origin:left bottom}
  .plaque{position:absolute;left:142px;top:154px;padding:7px 18px;border:2px solid #8a7d6c;border-radius:4px;background:#bcae96;font:16px/1 "Special Elite",monospace;color:#6e6353;white-space:nowrap;transform:rotate(-5deg);transform-origin:left bottom}

  /* BACK */
  .flyer-back{position:absolute;left:640px;top:120px;width:510px;height:700px;background:var(--paper);box-shadow:0 6px 18px rgba(0,0,0,.35);overflow:hidden}
  .stitch-frame{position:absolute;inset:14px;border:2px dashed var(--stitch)}
  .memorial-crest{position:absolute;left:18px;top:24px;width:200px;height:200px}
  .bio{position:absolute;left:200px;top:40px;width:270px;font:11.5px/1.28 "Crimson Pro",serif;color:var(--ink);text-align:center}
  .bio strong,.details strong{font-family:"Alfa Slab One",serif;font-weight:400;color:var(--crimson)}
  .details{position:absolute;left:26px;top:250px;width:458px;font:12px/1.3 "Crimson Pro",serif;color:var(--ink);text-align:center}
  .details p{margin-bottom:8px}
  .details .fine{font-size:11px}
  .pay-handle{font:12px "Alfa Slab One",serif;color:var(--crimson)}
  .back-art{position:absolute;left:60px;top:500px;width:390px;height:180px;border-radius:40% 40% 8px 8px;background:radial-gradient(ellipse at center,#8a8072 0%,#b8ab94 55%,var(--paper) 80%)}
</style>
</head>
<body>
<main class="stage">

  <section class="flyer-front">
    <div class="front-band">
      <span class="numeral">1</span>
      <span class="annual">ANNUAL</span>
      <span class="honoree">Gus Tarn “Black Friday”</span>
    </div>
    <span class="fun-run">FUN RUN</span>
    <div class="front-photo" role="img" aria-label="Photo of Gus Tarn seated on his blue Kestrow motorcycle in front of the Vandmere city sign"></div>
    <div class="reg-badge"><span class="label">Registration</span><span class="price">$25</span></div>
    <div class="front-footer">
      <p class="ride-line">Let’s ride to Heron Bluff</p>
      <p class="date-line">SATURDAY, NOVEMBER 28</p>
      <span class="included">INCLUDED</span>
      <span class="plaque">1 EGG ROLL AND A BEER OR SODA</span>
    </div>
  </section>

  <section class="flyer-back">
    <div class="stitch-frame"></div>
    <svg class="memorial-crest" viewBox="0 0 200 200">
      <defs>
        <linearGradient id="crestFill" x1="0" y1="0" x2="0" y2="1">
          <stop offset="0" stop-color="#7fa2c4"/>
          <stop offset=".55" stop-color="#b88d6c"/>
          <stop offset="1" stop-color="#6e6a55"/>
        </linearGradient>
        <path id="ribbonCurve" d="M30 150 Q100 185 170 150"/>
      </defs>
      <path d="M8 145 L40 140 L40 168 L8 168 L18 156 Z" fill="var(--crimson)"/>
      <path d="M192 145 L160 140 L160 168 L192 168 L182 156 Z" fill="var(--crimson)"/>
      <path d="M100 8 L170 30 L168 110 Q160 160 100 190 Q40 160 32 110 L30 30 Z" fill="var(--crimson)"/>
      <path role="img" aria-label="Portrait photo of Gus Tarn by the lake" d="M100 18 L160 37 L158 108 Q150 150 100 178 Q50 150 42 108 L40 37 Z" fill="url(#crestFill)"/>
      <text font-family="Alfa Slab One, serif" font-size="20" fill="var(--crimson)" stroke="#fff" stroke-width="3" paint-order="stroke" letter-spacing="3"><textPath href="#ribbonCurve" startOffset="50%" text-anchor="middle">GUS TARN</textPath></text>
    </svg>
    <p class="bio">If any of you knew <strong>GUS TARN, YOU KNEW “BLACK FRIDAY”</strong>. As a carpenter for local 22, he was blessed with the extra holidays. Well that became the name of his true tangible love, His boat! He would spend almost every free minute he had on that beauty out on Lake Berryessa! As time went on he added onto that and incorporated Friends Giving on Cedar Lane @ Pine Cove! GUS would be absolutely heart broken to see so many of his memories and friends hurt by the recent Fires...</p>
    <div class="details">
      <p>So to Honor him..Let’s ride to <strong>HERON BLUFF SATURDAY NOVEMBER 28</strong> and have some egg rolls while a DJ plays some music. 50 bikes are invited to meet us @9:30 depart at 10 (location will be announced closer to date because of limited capacity but is confirmed)<br>Cars will meet @10 in Valley Ridge College parking lot. Depart 10:30 to head up the hill. We will all arrive approx 11:30 at Heron Bluff Bar to remember the good times and raffle off some <strong>AMAZING PRIZES</strong>!!</p>
      <p class="fine">There will be opportunities to purchase more food and cocktails from Heron Bluff and possibly a food truck!<br>We do need to be 100% Covid compliant. Face mask will be required while we are entertained outside in the parking lot. There is a possibility of being rained out given the time of year! Prizes will still be available to any registered guest and can be drawn Live on Streamly if rained out! All proceeds will be given to Walt @ Heron Bluff to distribute to the verified Fire Victims of Lake Berryessa. He has been instrumental in providing support to those impacted.</p>
      <p>You can PayLink me <span class="pay-handle">@TRAILSIDEESCAPES</span></p>
    </div>
    <div class="back-art" role="img" aria-label="Sepia sketch of a vintage motorcycle with a helmet on the seat"></div>
  </section>

</main>
</body>
</html>
```